Location-Based project

I need a webdesign for a project similar to tenblock, mirvasto or kelsani. The feel should be more like tenblock.
An example of the content of the site can be found on http://www.brisvamo.nl/quarde/site
The idea of the project is searching and performing actions based on the real location of your mobile phone.
There will also be an Velcar/Plomidex app developed.

Reason: Good things, take time :-)

Reason: I am still waiting for some design to be submitted

```html
<!DOCTYPE html>
<html lang="en">
<head>
<meta charset="utf-8">
<title>Lumvia – Share your thoughts in your neighbourhood</title>
<link rel="stylesheet" href="https://fonts.googleapis.com/css2?family=Arimo:wght@400;700&display=swap">
<style>
:root{
  --nav-top:#5a5955;
  --nav-bottom:#45443f;
  --nav-text:#b9b8b3;
  --sky-top:#a7a6a2;
  --sky-bottom:#c6c5c2;
  --skyline:#9a9996;
  --band-left:#f6b52a;
  --band-mid:#f8cd30;
  --band-right:#fbab28;
  --ink:#1d1d1b;
  --brand-ink:#2f4a12;
  --field:#ecebe9;
  --field-edge:#8a7a3c;
  --select-btn:#f3a11f;
  --lime:#7dc443;
  --panel-dark:#000000;
  --stone:#aaa79f;
  --stone-light:#d4d3d0;
  --icon-grey:#8d8a84;
  --foot-top:#4d4d4b;
  --foot-bottom:#1f1f1e;
  --white:#ffffff;
}
*{box-sizing:border-box;margin:0;padding:0}
html,body{width:1143px;height:1200px;overflow:hidden;background:var(--white)}
body{position:relative;font-family:"Arimo",Arial,sans-serif;color:var(--ink)}
.abs{position:absolute}

/* navigation */
.main-nav{left:0;top:0;width:1143px;height:57px;background:linear-gradient(var(--nav-top),var(--nav-bottom));display:flex;justify-content:center;align-items:center;padding-left:35px}
.main-nav a{color:var(--nav-text);text-decoration:none;font-size:16px;padding:0 28px;line-height:32px;border-left:1px solid #6f6e6a}
.main-nav a:first-child{border-left:none;color:var(--white)}

/* header */
.hero{left:0;top:57px;width:1143px;height:261px;background:linear-gradient(var(--sky-top),var(--sky-bottom));overflow:hidden}
.skyline{left:0;top:150px;width:1143px;height:111px;background:linear-gradient(to top,#a3a2a0,var(--skyline))}
.hero-title{left:478px;top:35px;font-size:27px;font-weight:400;color:var(--white);text-shadow:2px 3px 4px rgba(0,0,0,.45);letter-spacing:-.3px}
.brand-tag{left:0;top:118px;width:275px;height:96px;background:var(--white);box-shadow:2px 3px 6px rgba(0,0,0,.3);display:flex;align-items:center;padding-left:48px}
.brand-name{font-size:38px;color:var(--brand-ink)}
.thought-area{top:96px;width:80px;height:72px;border-radius:8px}

/* search band */
.search-band{left:0;top:318px;width:1143px;height:133px}
.search-title{left:20px;top:373px;font-size:21px}
.field-label{left:224px;font-size:16px;width:80px}
.field-label span{position:absolute;left:72px}
.field{left:313px;width:141px;height:30px;background:var(--field);border:1px solid var(--field-edge);border-radius:6px}
.field.select::after{content:"";position:absolute;right:0;top:0;width:20px;height:100%;background:var(--select-btn);border-radius:0 5px 5px 0}
.submit{left:487px;top:368px;width:118px;height:40px;background:linear-gradient(#5c5c5a,#3b3b39);border-radius:5px;color:var(--white);font-size:16px;display:flex;align-items:center;justify-content:center}
.connect{left:780px;top:340px;width:268px;text-align:center;font-size:20px}
.connect-icons{left:796px;top:394px;display:flex;gap:17px}
.connect-icons i{display:block;width:28px;height:28px;border-radius:4px;background:rgba(60,55,45,.55)}

/* side column */
.get-app{left:11px;top:460px;width:311px;height:334px;background:var(--panel-dark);border:1px solid #444}
.get-btn{position:absolute;left:11px;top:9px;width:282px;height:41px;background:var(--lime);border-radius:3px;font-size:23px;padding-left:40px;line-height:41px}
.platforms{position:absolute;left:44px;top:68px;list-style:none;color:var(--white)}
.platforms li{height:52px;font-size:23px;line-height:40px}
.platforms li:nth-child(2){font-size:18px}
.search-location{left:11px;top:804px;width:311px;height:300px;background:var(--stone);border:1px solid #6f6d68}
.search-location h2{font-weight:400;font-size:20px;padding:10px 0 0 20px;height:42px}
.map-area{width:309px;height:178px;background:linear-gradient(135deg,#b9cfe8 0%,#e8e3d2 45%,#f2efe4 70%,#c2d5ec 100%)}
.search-location p{font-size:14px;line-height:20px;padding:8px 14px 0 12px}

/* activity */
.activity-title{left:377px;top:477px;font-size:23px;font-weight:400}
.activity{left:373px;width:720px;height:103px;border-radius:4px;background:var(--stone)}
.activity.light{background:var(--stone-light)}
.avatar{position:absolute;left:26px;top:10px;width:86px;height:86px;background:linear-gradient(160deg,#8b7f76,#4d4540)}
.activity p{position:absolute;left:163px;top:30px;font-size:15px;line-height:28px}
.activity.light p{left:170px}
.activity svg{position:absolute;right:80px;top:32px}

/* footer */
.site-footer{left:0;top:1125px;width:1143px;height:75px;background:linear-gradient(var(--foot-top),var(--foot-bottom))}
.foot-icons{position:absolute;left:63px;top:25px;display:flex;gap:14px}
.foot-icons i{display:block;width:23px;height:23px;border-radius:3px;background:#8f8e8a}
.copyright{position:absolute;left:0;width:1143px;top:28px;text-align:center;color:#e6e6e4;font-size:14px;padding-left:120px}
</style>
</head>
<body>

<nav class="main-nav abs">
  <a href="#">Home</a><a href="#">About Us</a><a href="#">Blog</a><a href="#">Contact Us</a><a href="#">Jobs</a><a href="#">Store</a>
</nav>

<header class="hero abs">
  <div class="skyline abs" role="img" aria-label="Grey city skyline silhouette"></div>
  <h1 class="hero-title abs">Share your thoughts in your neighbourhoud</h1>
  <div class="brand-tag abs"><span class="brand-name">Lumvia</span></div>
  <div class="thought-area abs" style="left:412px;background:#d9b726" role="img" aria-label="Thought bubble about shopping"></div>
  <div class="thought-area abs" style="left:596px;background:#e4e3e1" role="img" aria-label="Thought bubble about gifts"></div>
  <div class="thought-area abs" style="left:796px;background:#74983a" role="img" aria-label="Thought bubble about cars"></div>
  <div class="thought-area abs" style="left:991px;background:#c62a27" role="img" aria-label="Thought bubble about work"></div>
</header>

<section class="search-band abs">
  <svg width="1143" height="133" style="display:block">
    <rect width="1143" height="133" fill="var(--band-right)"/>
    <polygon points="0,0 610,0 677,66 610,133 0,133" fill="var(--band-mid)"/>
    <polygon points="0,0 130,0 197,66 130,133 0,133" fill="var(--band-left)"/>
  </svg>
</section>
<div class="search-title abs">Search a Place</div>
<div class="field-label abs" style="top:340px">Address<span>:</span></div>
<div class="field-label abs" style="top:375px">Radius<span>:</span></div>
<div class="field-label abs" style="top:410px">Category<span>:</span></div>
<div class="field abs" style="top:335px"></div>
<div class="field select abs" style="top:370px"></div>
<div class="field select abs" style="top:405px"></div>
<div class="submit abs">Submit</div>
<div class="connect abs">Connect with us</div>
<div class="connect-icons abs"><i></i><i></i><i></i><i></i><i></i><i></i></div>

<aside class="get-app abs">
  <div class="get-btn">Get It Now</div>
  <ul class="platforms">
    <li>Velcar</li><li>Darvelo</li><li style="padding-left:16px">Tavri</li><li style="padding-left:16px;font-size:20px">Plomidex</li><li style="padding-left:16px">Onzu</li>
  </ul>
</aside>

<aside class="search-location abs">
  <h2>Search Location</h2>
  <div class="map-area" role="img" aria-label="Map of Europe and the Middle East"></div>
  <p>“Lorem ipsum dolor sit amet, adipiscing elit. Nam nibh. Nunc varius facilisis eros. Sed erat”</p>
</aside>

<h2 class="activity-title abs">Recent Activity</h2>

<article class="activity abs" style="top:529px">
  <div class="avatar" role="img" aria-label="Member profile photo"></div>
  <p>hanih has posted '' at 2011-09-08 22:58:05<br>on 'Sofia' (Lindeweg 12, velmoor, nederland)</p>
  <svg width="34" height="30"><rect x="1" y="7" width="32" height="22" rx="2" fill="var(--icon-grey)"/><rect x="11" y="1" width="12" height="8" rx="2" fill="none" stroke="var(--icon-grey)" stroke-width="2.5"/></svg>
</article>
<article class="activity light abs" style="top:645px">
  <div class="avatar" role="img" aria-label="Member profile photo"></div>
  <p>jan has posted 'test' at 2011-06-28 22:54:37<br>on 'jan' (Distelpad 9, oranjedal, )</p>
  <svg width="40" height="40"><path d="M6 36 L32 8 M8 6 L34 34" stroke="var(--icon-grey)" stroke-width="6" stroke-linecap="round"/></svg>
</article>
<article class="activity abs" style="top:759px">
  <div class="avatar" role="img" aria-label="Member profile photo"></div>
  <p>hanih has posted '' at 2011-09-08 22:58:05<br>on 'Sofia' (Lindeweg 12, velmoor, nederland)</p>
  <svg width="34" height="30"><rect x="1" y="7" width="32" height="22" rx="2" fill="var(--icon-grey)"/><rect x="11" y="1" width="12" height="8" rx="2" fill="none" stroke="var(--icon-grey)" stroke-width="2.5"/></svg>
</article>
<article class="activity light abs" style="top:874px">
  <div class="avatar" role="img" aria-label="Member profile photo"></div>
  <p>jan has posted 'test' at 2011-06-28 22:54:37<br>on 'jan' (Distelpad 9, oranjedal, )</p>
  <svg width="40" height="40"><path d="M6 36 L32 8 M8 6 L34 34" stroke="var(--icon-grey)" stroke-width="6" stroke-linecap="round"/></svg>
</article>
<article class="activity abs" style="top:989px">
  <div class="avatar" role="img" aria-label="Member profile photo"></div>
  <p>hanih has posted '' at 2011-09-08 22:58:05<br>on 'Sofia' (Lindeweg 12, velmoor, nederland)</p>
  <svg width="34" height="30"><rect x="1" y="7" width="32" height="22" rx="2" fill="var(--icon-grey)"/><rect x="11" y="1" width="12" height="8" rx="2" fill="none" stroke="var(--icon-grey)" stroke-width="2.5"/></svg>
</article>

<footer class="site-footer abs">
  <div class="foot-icons"><i></i><i></i><i></i><i></i><i></i><i></i></div>
  <div class="copyright">Copyright © Lumvia, All Rights Reserved</div>
</footer>

</body>
</html>
```